Business Card Design - Pediatric Dentist

We need a business card for a new dental office. We are a pediatric dentist in Austin Tx. I would like a design that use bright green and if possible light blue.

Target Market(s)

Marketed to young moms

Industry/Entity Type

Dental

Contact Information for Business Card

Marcus Hollin DDS
Tidewell Pediatric Dentistry
438 E. Corvell Lane. Austin TX 78731
(512) 284 9153.

In the back i would like to state "we take most insurances, Chip & Medicaid" & a map

Colors
add136
cadf82
85cae6

```html
<!DOCTYPE html>
<html lang="en">
<head>
<meta charset="utf-8">
<title>Tidewell Pediatric Dentistry – Business Card</title>
<link rel="stylesheet" href="https://fonts.googleapis.com/css2?family=Archivo+Narrow:wght@400;700&display=swap">
<style>
  :root {
    --green: #34b44a;
    --lime: #add136;
    --pale-green: #cadf82;
    --sky: #35b6e9;
    --pale-sky: #85cae6;
    --paper: #ffffff;
    --backdrop: #e8e8e5;
    --map-tone: #e6e2da;
  }
  * { box-sizing: border-box; margin: 0; padding: 0; }
  html, body {
    width: 1200px; height: 1000px; overflow: hidden;
    background: var(--backdrop);
    font-family: "Archivo Narrow", "Arial Narrow", sans-serif;
  }
  .canvas { position: relative; width: 1200px; height: 1000px; }
  .card {
    position: absolute; left: 250px; width: 700px; height: 400px;
    background: var(--paper); overflow: hidden;
    box-shadow: 0 6px 18px rgba(0,0,0,0.15);
  }
  .card--back { top: 70px; }
  .card--front { top: 530px; display: flex; align-items: center; justify-content: center; gap: 28px; }

  .backdrop-wash {
    position: absolute; left: 0; top: 0; width: 480px; height: 400px;
    background: radial-gradient(ellipse at 35% 55%, rgba(202,223,130,0.45), rgba(133,202,230,0.25) 55%, rgba(255,255,255,0) 80%);
  }
  .headline {
    position: absolute; left: 34px; top: 22px;
    font-weight: 700; font-size: 62px; line-height: 1; letter-spacing: -1px;
    color: var(--green); text-transform: uppercase;
  }
  .route-arrow { position: absolute; left: 0; top: 0; width: 700px; height: 400px; }
  .contact-list {
    position: absolute; left: 34px; top: 128px; list-style: none;
  }
  .contact-list li {
    display: flex; align-items: center; gap: 8px;
    font-weight: 700; font-size: 28px; line-height: 36px; letter-spacing: -0.5px;
    color: var(--green); text-transform: uppercase;
  }
  .contact-list svg { width: 16px; height: 16px; flex: none; }
  .coverage-note {
    position: absolute; left: 190px; top: 302px;
    font-size: 12px; font-weight: 700; color: var(--sky); text-transform: uppercase;
  }
  .map-area {
    position: absolute; left: 470px; top: 240px; width: 205px; height: 138px;
    background: linear-gradient(135deg, var(--map-tone), #d9d5cc);
    border: 1px solid #cfcac0;
  }
  .brand-dot { width: 60px; height: 60px; border-radius: 50%; background: var(--green); }
  .brand-name {
    font-weight: 700; font-size: 50px; line-height: 1.05; color: var(--green);
  }
</style>
</head>
<body>
<main class="canvas">
  <section class="card card--back">
    <div class="backdrop-wash"></div>
    <h1 class="headline">Here we are!</h1>
    <svg class="route-arrow" viewBox="0 0 700 400" aria-hidden="true">
      <path d="M30 98 H545 V212" fill="none" stroke="var(--sky)" stroke-width="12"/>
      <polygon points="522,208 568,208 545,240" fill="var(--sky)"/>
    </svg>
    <ul class="contact-list">
      <li><svg viewBox="0 0 20 20"><polygon points="10,1 12.6,7 19,7.4 14,11.6 15.6,18 10,14.5 4.4,18 6,11.6 1,7.4 7.4,7" fill="var(--sky)"/></svg>Marcus Hollin DDS</li>
      <li><svg viewBox="0 0 20 20"><polygon points="10,1 12.6,7 19,7.4 14,11.6 15.6,18 10,14.5 4.4,18 6,11.6 1,7.4 7.4,7" fill="var(--sky)"/></svg>Tidewell Pediatric Dentistry</li>
      <li><svg viewBox="0 0 20 20"><polygon points="10,1 12.6,7 19,7.4 14,11.6 15.6,18 10,14.5 4.4,18 6,11.6 1,7.4 7.4,7" fill="var(--sky)"/></svg>438 E. Corvell Lane. Austin TX 78731</li>
      <li><svg viewBox="0 0 20 20"><polygon points="10,1 12.6,7 19,7.4 14,11.6 15.6,18 10,14.5 4.4,18 6,11.6 1,7.4 7.4,7" fill="var(--sky)"/></svg>(512) 284 9153</li>
    </ul>
    <p class="coverage-note">*We take most insurances, CHIP &amp; Medicaid</p>
    <div class="map-area" role="img" aria-label="Street map showing the office location"></div>
  </section>

  <section class="card card--front">
    <span class="brand-dot" aria-hidden="true"></span>
    <h2 class="brand-name">Tidewell<br>Pediatric<br>Dentistry</h2>
  </section>
</main>
</body>
</html>
```